Corvessa Glowroom - new approach for face and bodycare cosmetic products

Project Overview: We are re-designing a natural skincare brand called Corvessa. Our face and bodycare cosmetic products are made from a rich blend of natural ingredients, reminiscent of the colorful, vibrant, and refreshing character of cocktails. Taking a new approach to addressing the cosmetics audience, Corvessa is preparing to enter the market through the world of cocktails. Unlike most of the market, Corvessa offers complex formulas that have been expertly blended for maximum effect - just like a cocktail. We would like the branding and packaging to reflect this unique concept – evoking the fresh, playful, and luxurious cocktail lifestyle through colors, patterns, and style. The target is to make Corvessa a love brand and the design should help it.

What We Need:
Package design. Packaging design templates for a product line of 15–20 items (serums, creams, scrubs, etc.), with the potential to expand the portfolio in the future. Please use the packages (bottle and cardbox) attached.
Optional: Logo design derived from the current one (attached).

A cohesive visual identity that can be applied across future products and marketing materials.
The expected characteristics of Corvessa's new brand personality: playful, fun, easily customizable, strong and memorable visual appearance, great potential in branding, storytelling, visuality and community building, and a distinctive brand image.

Deliverables (in PPT or PDF):

Brand color palette and font selection.
Packaging design mockups (we can provide templates or die lines as needed).
Style guide or brand board (optional but preferred).

Target Market(s)

Targeted markets are EU countries. Target audience: Women aged 30+ who appreciate self-care, quality natural products, and beautiful design.

Industry/Entity Type

Skincare

Font styles to use
Serif
Decorative

Requirements
Must have
• Design Directions are as follows: a) Inspiration: Cocktail aesthetics – fresh fruits, vibrant colors, layered textures, playful elegance. b) Style: Modern, clean, nature-inspired, with a sense of indulgence and joy. Color palette: Bright and fresh tones (think citrus, berry, mint, tropical vibes), but with flexibility for product differentiation.
Nice to have
• Corvessa uses fresh colors, like a cocktail menu, with cocktail accessories and shades of their decorative elements.

```html
<!DOCTYPE html>
<html lang="en">
<head>
<meta charset="utf-8">
<title>Corvessa Glowroom – Packaging Design Mockup Preview</title>
<link rel="stylesheet" href="https://fonts.googleapis.com/css2?family=Arimo&family=Gilda+Display&family=Montserrat:wght@500;600;700&display=swap">
<style>
  :root {
    --page: #ffffff;
    --stage: #f4f0dc;
    --stage-floor: #f8f5e6;
    --card: #fbf8ec;
    --ink: #1d4f55;
    --ink-soft: #2e5f63;
    --mint: #c2e8d3;
    --mint-deep: #a9dcc3;
    --coral: #f08a72;
    --coral-soft: #f6a48d;
    --leaf: #b9dca0;
    --leaf-2: #a9d395;
    --teal: #5fb0aa;
    --glass: #f3d98a;
    --cap: #ffffff;
    --cap-shade: #ecebe6;
    --jar-base: #e6e7a8;
  }
  * { box-sizing: border-box; margin: 0; padding: 0; }
  html, body { width: 1200px; height: 1200px; overflow: hidden; background: var(--page); }
  .canvas { position: relative; width: 1200px; height: 1200px; background: var(--page); }

  .page-title {
    position: absolute; top: 62px; left: 0; width: 100%;
    text-align: center; font-family: "Arimo", Arial, sans-serif;
    font-size: 25px; color: #111; 
  }

  .stage {
    position: absolute; left: 75px; top: 160px; width: 1074px; height: 1008px;
    background: var(--stage); overflow: hidden;
  }
  .stage-floor {
    position: absolute; left: 0; bottom: 0; width: 100%; height: 112px;
    background: var(--stage-floor);
  }

  /* Brand board */
  .brand-board {
    position: absolute; left: 209px; top: 68px; width: 656px; height: 830px;
    background: var(--card);
  }
  .brand-mark {
    position: absolute; left: 0; top: 80px; width: 100%;
    display: flex; justify-content: center;
  }
  .brand-dot { width: 56px; height: 56px; border-radius: 50%; background: var(--coral); }
  .brand-name {
    position: absolute; left: 0; top: 160px; width: 100%; text-align: center;
    font-family: "Gilda Display", Georgia, serif; font-size: 92px; line-height: 1;
    color: var(--ink);
  }
  .brand-tagline {
    position: absolute; left: 0; top: 262px; width: 100%; text-align: center;
    font-family: "Montserrat", Arial, sans-serif; font-weight: 600; font-size: 21px;
    letter-spacing: 0.24em; color: var(--ink);
  }

  .style-panel {
    position: absolute; left: 102px; top: 325px; width: 454px; height: 312px;
    border: 1.5px solid var(--ink-soft); border-radius: 6px;
  }
  .swatches { position: absolute; left: 44px; top: 24px; display: flex; gap: 11px; }
  .swatch { width: 48px; height: 48px; border-radius: 50%; }
  .swatch--leaf { background: var(--leaf); }
  .swatch--leaf-2 { background: var(--leaf-2); }
  .swatch--coral { background: var(--coral); }
  .swatch--teal { background: var(--teal); }
  .panel-label {
    position: absolute; left: 42px; font-family: "Montserrat", Arial, sans-serif;
    font-weight: 600; color: var(--ink); letter-spacing: 0.12em;
  }
  .panel-label--palette { top: 94px; font-size: 17px; }
  .panel-label--serif { top: 176px; font-size: 17px; letter-spacing: 0.1em; }
  .serif-sample {
    position: absolute; left: 40px; top: 118px; font-family: "Gilda Display", Georgia, serif;
    font-size: 46px; color: var(--ink); line-height: 1;
  }
  .serif-caps {
    position: absolute; left: 40px; top: 222px; font-family: "Gilda Display", Georgia, serif;
    font-size: 24px; color: var(--ink); letter-spacing: 0.02em;
  }
  .sans-sample {
    position: absolute; left: 40px; top: 256px; font-family: "Montserrat", Arial, sans-serif;
    font-weight: 500; font-size: 18px; color: var(--ink);
  }

  /* Packaging */
  .pack { position: absolute; }
  .art { position: absolute; border-radius: 8px; }
  .pack-title, .pack-sub {
    position: absolute; left: 0; width: 100%; text-align: center;
    font-family: "Montserrat", Arial, sans-serif; color: var(--ink);
  }

  .serum { left: 49px; top: 372px; width: 178px; height: 570px; }
  .serum-pump {
    position: absolute; left: 50px; top: 0; width: 78px; height: 158px;
    background: linear-gradient(90deg, #eef1f1, #fafafa 50%, #e9ecec);
    border-radius: 6px 6px 0 0; border: 1px solid #e2e4e4;
  }
  .serum-collar {
    position: absolute; left: 36px; top: 150px; width: 106px; height: 70px;
    background: linear-gradient(90deg, #e6e6e6, #fbfbfb 45%, #e3e3e3);
  }
  .serum-glass {
    position: absolute; left: 0; top: 216px; width: 178px; height: 354px;
    background: var(--glass); border-radius: 42px 42px 12px 12px;
  }
  .serum-label {
    position: absolute; left: 0; top: 216px; width: 178px; height: 328px;
    background: var(--mint);
  }
  .serum-label .art { left: 22px; top: 20px; width: 134px; height: 130px;
    background: radial-gradient(circle at 30% 60%, #f2a15a 0 22%, transparent 23%),
                radial-gradient(circle at 72% 52%, #f6c64c 0 22%, transparent 23%),
                var(--mint-deep); }
  .serum-label .pack-title { top: 160px; font-weight: 700; font-size: 27px; line-height: 1.28; letter-spacing: 0.08em; }
  .serum-label .pack-sub { top: 236px; font-weight: 600; font-size: 19px; letter-spacing: 0.14em; }
  .serum-label .art--small { left: 62px; top: 274px; width: 54px; height: 28px; border-radius: 50%; background: var(--mint-deep); }

  .jar { left: 250px; top: 702px; width: 322px; height: 248px; }
  .jar-lid {
    position: absolute; left: 0; top: 0; width: 322px; height: 70px;
    background: linear-gradient(180deg, var(--cap), var(--cap-shade));
    border-radius: 14px 14px 6px 6px;
  }
  .jar-body {
    position: absolute; left: 0; top: 70px; width: 322px; height: 178px;
    background: var(--jar-base); border-radius: 4px 4px 16px 16px;
  }
  .jar-label {
    position: absolute; left: 0; top: 83px; width: 322px; height: 146px;
    background: var(--coral);
  }
  .jar-label .art { left: 116px; top: 20px; width: 90px; height: 42px; background: var(--coral-soft); }
  .jar-label .art--left { left: 24px; top: 30px; width: 60px; height: 90px; }
  .jar-label .art--right { left: 248px; top: 26px; width: 56px; height: 90px; }
  .jar-label .pack-title { top: 74px; font-weight: 700; font-size: 21px; letter-spacing: 0.08em; color: var(--card); }
  .jar-label .pack-sub { top: 108px; font-weight: 500; font-size: 19px; letter-spacing: 0.14em; color: var(--card); }

  .tube { clip-path: polygon(0 0, 100% 0, 92% 82%, 92% 100%, 8% 100%, 8% 82%); }
  .tube-crimp { position: absolute; left: 0; top: 0; width: 100%; height: 20px; }
  .tube-body { position: absolute; left: 0; top: 20px; width: 100%; }
  .tube-cap {
    position: absolute; bottom: 0; left: 8%; width: 84%;
    background: linear-gradient(90deg, #ededed, #fff 45%, #e8e8e8); border-radius: 0 0 8px 8px;
  }

  .berry { left: 628px; top: 427px; width: 210px; height: 510px; }
  .berry .tube-crimp { background: var(--coral); }
  .berry .tube-body { height: 398px; background: linear-gradient(90deg, var(--coral), var(--coral-soft)); }
  .berry .tube-cap { height: 92px; }
  .berry .art { left: 58px; top: 90px; width: 98px; height: 110px; background: #ec7d66; border-radius: 40%; }
  .berry .art--faint { left: 70px; top: 300px; width: 70px; height: 80px; background: #f4987f; }
  .berry .pack-title { top: 216px; font-weight: 700; font-size: 29px; letter-spacing: 0.06em; }
  .berry .pack-sub { top: 258px; font-weight: 600; font-size: 15px; letter-spacing: 0.13em; }

  .daycream { left: 828px; top: 360px; width: 194px; height: 550px; }
  .daycream .tube-crimp { background: var(--mint-deep); }
  .daycream .tube-body { height: 440px; background: linear-gradient(90deg, var(--mint-deep), var(--mint)); }
  .daycream .tube-cap { height: 94px; }
  .daycream .art { left: 64px; top: 80px; width: 66px; height: 96px; background: #99d2b6; }
  .daycream .art--faint { left: 60px; top: 290px; width: 70px; height: 90px; background: #b3e0c8; }
  .daycream .pack-title { top: 198px; font-weight: 600; font-size: 20px; letter-spacing: 0.06em; }
  .daycream .pack-sub { top: 228px; font-weight: 600; font-size: 15px; letter-spacing: 0.1em; }
</style>
</head>
<body>
<main class="canvas">
  <h1 class="page-title">Packaging Design Mockup Preview</h1>

  <section class="stage">
    <div class="stage-floor"></div>

    <article class="brand-board">
      <div class="brand-mark"><span class="brand-dot"></span></div>
      <p class="brand-name">Corvessa</p>
      <p class="brand-tagline">NATURAL SKINCARE</p>

      <div class="style-panel">
        <div class="swatches">
          <span class="swatch swatch--leaf"></span>
          <span class="swatch swatch--leaf-2"></span>
          <span class="swatch swatch--coral"></span>
          <span class="swatch swatch--teal"></span>
        </div>
        <p class="panel-label panel-label--palette">COLOR PALETTE</p>
        <p class="serif-sample">Corvessa</p>
        <p class="panel-label panel-label--serif">SERIF TYPEFACE</p>
        <p class="serif-caps">NATURAL SKINCARE</p>
        <p class="sans-sample">Sans-Serif Typeface</p>
      </div>
    </article>

    <div class="pack serum">
      <div class="serum-pump"></div>
      <div class="serum-collar"></div>
      <div class="serum-glass"></div>
      <div class="serum-label">
        <div class="art" role="img" aria-label="Illustration of a cocktail glass with citrus slices and leaves"></div>
        <p class="pack-title">CITRUS<br>GLOW</p>
        <p class="pack-sub">SERUM</p>
        <div class="art art--small" role="img" aria-label="Small leaf illustration"></div>
      </div>
    </div>

    <div class="pack jar">
      <div class="jar-lid"></div>
      <div class="jar-body"></div>
      <div class="jar-label">
        <div class="art" role="img" aria-label="Line illustration of an olive sprig"></div>
        <div class="art art--left" role="img" aria-label="Faint leaf illustration"></div>
        <div class="art art--right" role="img" aria-label="Faint leaf illustration"></div>
        <p class="pack-title">REVITALIZING</p>
        <p class="pack-sub">FACE CREAM</p>
      </div>
    </div>

    <div class="pack berry">
      <div class="tube" style="position:absolute;inset:0;">
        <div class="tube-crimp"></div>
        <div class="tube-body">
          <div class="art" role="img" aria-label="Line illustration of strawberries"></div>
          <p class="pack-title">BERRY</p>
          <p class="pack-sub">BODY SCRUB</p>
          <div class="art art--faint" role="img" aria-label="Faint leaf sprig illustration"></div>
        </div>
        <div class="tube-cap"></div>
      </div>
    </div>

    <div class="pack daycream">
      <div class="tube" style="position:absolute;inset:0;">
        <div class="tube-crimp"></div>
        <div class="tube-body">
          <div class="art" role="img" aria-label="Line illustration of an olive branch"></div>
          <p class="pack-title">NOURISHING</p>
          <p class="pack-sub">DAY CREAM</p>
          <div class="art art--faint" role="img" aria-label="Faint olive branch illustration"></div>
        </div>
        <div class="tube-cap"></div>
      </div>
    </div>
  </section>
</main>
</body>
</html>
```